Introduction:
We are an Australia-based Cyber Security Penetration testing company seeking a website redesign to showcase our services, expertise, and experience. Our target audience includes businesses and organizations of all sizes who are seeking to secure their IT infrastructure against cyber threats. The purpose of the website redesign is to increase our online presence, generate leads, and establish our company as a trusted authority in the industry.
Objectives:
Create a professional and modern website that is easy to navigate and user-friendly.
Provide information about our company, services, and expertise.
Clearly display table of our 3 services: Bug Bounty as a Service, Penetration Testing and Code Review.
Generate leads through online contact forms and calls-to-action.
Optimize the website for search engines to increase visibility and traffic.
Website similar to: https://www.velmoro.com.au/.
Target Audience:
Our target audience includes businesses and organizations of all sizes that require cybersecurity penetration testing services. These include:
Small and medium-sized enterprises (SMEs)
Australian Government agencies
Design Requirements:
Clean, modern, and professional design.
Use of colors that convey trust, reliability, and expertise (such as orange and grey).
Calls-to-action that encourage visitors to contact us or request a quote.
Integration with social media channels to increase engagement and brand awareness.
A blog section to showcase our thought leadership and expertise.
A news section to share updates about our company and the industry.
Content Requirements:
Home page that introduces our company and services and highlights our expertise.
About Us page that provides information about our company, team, and values.
Services page that lists our services and explains the benefits of each.
Case Studies page that showcases our previous work and success stories.
Contact Us page that includes a contact form, phone number, and email address.
Blog section with articles related to the cybersecurity industry and our services.
News section with updates about our company and the industry.
Look and feel
Each slider illustrates characteristics of the customer's brand and the style your logo design should communicate.

```html
<!DOCTYPE html>
<html lang="en">
<head>
<meta charset="utf-8">
<title>Emberstrata — Cyber Security</title>
<link href="https://fonts.googleapis.com/css2?family=Exo:wght@400;500;600;700&display=swap" rel="stylesheet">
<style>
:root{
  --orange:#f26b3a;
  --orange-dark:#d9572a;
  --ink:#2f3133;
  --charcoal:#333436;
  --night:#232426;
  --grey:#7a7c80;
  --line:#e4e4e4;
  --paper:#ffffff;
  --mist:#f4f4f4;
}
*{box-sizing:border-box;margin:0;padding:0}
html,body{width:1200px;height:2516px;overflow:hidden;background:var(--paper)}
body{font-family:"Exo",sans-serif;color:var(--ink);font-size:13px;line-height:1.6}
.wrap{width:1040px;margin:0 auto;position:relative;height:100%}
.tag{display:inline-block;border:1px solid var(--line);color:var(--grey);font-size:10px;letter-spacing:1px;text-transform:uppercase;padding:2px 12px;border-radius:2px}
.btn{display:inline-block;background:var(--orange);color:#fff;font-size:11px;font-weight:600;letter-spacing:.5px;text-transform:uppercase;padding:10px 22px;border-radius:2px}
.btn.ghost{background:transparent;border:1px solid #fff}
.muted{color:var(--grey)}

/* nav */
.site-nav{height:70px;border-bottom:1px solid var(--line)}
.site-nav .wrap{display:flex;align-items:center;justify-content:space-between}
.brand{display:flex;align-items:center;gap:8px;font-weight:700;font-size:20px;color:var(--orange)}
.brand-dot{width:14px;height:14px;border-radius:50%;background:var(--orange)}
.nav-links{display:flex;gap:34px;font-size:11px;font-weight:600;text-transform:uppercase;letter-spacing:.6px;color:var(--ink)}
.nav-links .active{color:var(--orange)}
.nav-cta{border:1px solid var(--orange);color:var(--orange);font-size:11px;font-weight:600;padding:7px 16px;text-transform:uppercase}

/* hero */
.hero{height:490px;background:linear-gradient(100deg,#1d1e20 0%,#3a3b3e 55%,#55575b 100%);position:relative;color:#fff}
.hero .wrap{padding-top:120px}
.hero-eyebrow{display:inline-block;background:var(--orange);font-size:10px;padding:2px 10px;text-transform:uppercase;letter-spacing:1px}
.hero h1{font-size:58px;line-height:1.05;font-weight:700;margin:18px 0 22px;width:520px}
.hero p{width:440px;font-size:13px;color:#d8d8d8;margin-bottom:26px}

/* about */
.about{height:260px;border-bottom:1px solid var(--line)}
.about .wrap{display:grid;grid-template-columns:250px 250px 250px 1fr;gap:30px;padding-top:50px}
.about p{font-size:11px;color:var(--grey);margin-bottom:14px}
.about h4{font-size:13px;font-weight:600;margin-bottom:2px}
.about .link{font-size:10px;color:var(--orange);display:block;margin-bottom:16px}
.about h2{font-size:32px;line-height:1.1;font-weight:700;margin-top:10px;border-left:3px solid var(--orange);padding-left:14px}

/* solutions */
.solutions{height:270px;display:flex}
.solutions-lead{width:260px;background:var(--orange);color:#fff;padding:50px 0 0 80px}
.solutions-lead .tag{color:#fff;border-color:rgba(255,255,255,.6)}
.solutions-lead h2{font-size:32px;line-height:1.1;font-weight:700;margin-top:14px}
.service-cards{flex:1;display:grid;grid-template-columns:repeat(3,1fr);background:var(--mist)}
.service{padding:46px 40px;border-right:1px solid var(--line)}
.service h3{font-size:16px;font-weight:600;margin:14px 0 8px}
.service p{font-size:11px;color:var(--grey);margin-bottom:16px}
.service .more{font-size:10px;color:var(--orange);font-weight:600;text-transform:uppercase}

/* partner */
.partner{height:360px;background:linear-gradient(90deg,#1b1c1e 0%,#2e2f32 60%,#27282a 100%);color:#fff;position:relative}
.partner-texture{position:absolute;left:0;top:0;width:58%;height:100%;background:linear-gradient(135deg,#2c2d30,#1f2022 60%,#35363a)}
.partner-copy{position:absolute;left:660px;top:100px;width:360px}
.partner h2{font-size:30px;line-height:1.15;font-weight:700;margin-bottom:16px}
.partner p{font-size:11px;color:#bdbdbd;margin-bottom:24px}
.partner .actions{display:flex;gap:14px}

/* consulting */
.consulting{height:440px;text-align:center}
.consulting .wrap{padding-top:70px}
.consulting h2{font-size:30px;line-height:1.15;font-weight:700;margin:14px auto 50px;width:420px}
.pillars{display:grid;grid-template-columns:repeat(3,1fr);gap:40px;text-align:left}
.pillar{display:flex;gap:16px}
.pillar h3{font-size:14px;font-weight:600;margin-bottom:6px}
.pillar p{font-size:11px;color:var(--grey)}
.consulting .note{font-size:11px;color:var(--grey);width:620px;margin:50px auto 0}

/* contact */
.contact{height:380px;border-top:1px solid var(--line)}
.contact .wrap{display:grid;grid-template-columns:420px 1fr;gap:60px;padding-top:50px}
.contact h2{font-size:32px;line-height:1.1;font-weight:700;margin:12px 0 22px}
.contact-photo{width:340px;height:170px;background:linear-gradient(120deg,#c9cdd2,#e6a27f 55%,#f0ede9)}
.contact-form{display:grid;grid-template-columns:1fr 1fr;gap:14px 24px}
.field label{display:block;font-size:10px;color:var(--grey);margin-bottom:4px}
.field span{display:block;height:30px;border:1px solid var(--line)}
.field.full{grid-column:1 / -1}
.field.full span{height:60px}

/* footer */
.site-footer{height:246px;background:var(--charcoal);color:#d0d0d0}
.site-footer .wrap{display:grid;grid-template-columns:1fr 180px 180px 220px;padding-top:50px;height:196px}
.site-footer .brand{font-size:18px}
.socials{display:flex;gap:8px;margin-top:16px}
.socials i{width:24px;height:24px;border-radius:50%;background:#4a4b4e;display:block}
.site-footer h4{color:#fff;font-size:14px;font-weight:600;margin-bottom:12px}
.site-footer li{list-style:none;font-size:11px;margin-bottom:6px}
.site-footer li::before{content:"";display:inline-block;width:5px;height:5px;background:var(--orange);margin-right:8px;vertical-align:middle}
.footer-bar{height:50px;border-top:1px solid #47484b}
.footer-bar .wrap{display:flex;justify-content:space-between;align-items:center;font-size:10px;color:#9a9a9a}
</style>
</head>
<body>

<header class="site-nav">
  <div class="wrap">
    <div class="brand"><span class="brand-dot"></span>Emberstrata</div>
    <nav class="nav-links">
      <span class="active">Home</span><span>About</span><span>Services</span><span>Case Studies</span><span>Blog</span><span>News</span><span>Contact</span>
    </nav>
    <span class="nav-cta">Request a Quote</span>
  </div>
</header>

<section class="hero" role="img" aria-label="Photo of two security analysts working at a laptop">
  <div class="wrap">
    <span class="hero-eyebrow">Cyber Security</span>
    <h1>Shielding Your Digital World</h1>
    <p>Australian penetration testing specialists helping businesses and government agencies find weaknesses before attackers do, with clear reporting and practical fixes.</p>
    <span class="btn">Read More</span>
  </div>
</section>

<section class="about">
  <div class="wrap">
    <div>
      <p>We test networks, applications and cloud platforms with the same methods real attackers use, then explain the results in plain language.</p>
      <p>Our certified team works with firms of every size across Australia.</p>
    </div>
    <div>
      <h4>Cyber Security Threats</h4><span class="link">Learn more</span>
      <h4>Penetration Testing Steps</h4><span class="link">Learn more</span>
    </div>
    <div>
      <p>Each engagement is scoped to your risk, delivered on schedule and followed by a retest once fixes are in place.</p>
    </div>
    <div>
      <span class="tag">About Us</span>
      <h2>Leadership &amp; Expertise</h2>
    </div>
  </div>
</section>

<section class="solutions">
  <div class="solutions-lead">
    <span class="tag">Services</span>
    <h2>Solutions We Provide</h2>
  </div>
  <div class="service-cards">
    <div class="service">
      <svg width="34" height="34" viewBox="0 0 34 34" fill="none" stroke="#f26b3a" stroke-width="2"><circle cx="17" cy="17" r="14"/><circle cx="17" cy="17" r="6"/></svg>
      <h3>Bug Bounty</h3>
      <p>Managed programs that reward trusted researchers for finding flaws in your systems.</p>
      <span class="more">Read More</span>
    </div>
    <div class="service">
      <svg width="34" height="34" viewBox="0 0 34 34" fill="none" stroke="#f26b3a" stroke-width="2"><rect x="5" y="8" width="24" height="18"/><path d="M5 14h24"/></svg>
      <h3>Penetration Testing</h3>
      <p>Hands-on testing of networks and applications to expose real, exploitable risk.</p>
      <span class="more">Read More</span>
    </div>
    <div class="service">
      <svg width="34" height="34" viewBox="0 0 34 34" fill="none" stroke="#f26b3a" stroke-width="2"><path d="M12 10l-7 7 7 7M22 10l7 7-7 7"/></svg>
      <h3>Code Review</h3>
      <p>Line-by-line source review that catches insecure logic before it ships.</p>
      <span class="more">Read More</span>
    </div>
  </div>
</section>

<section class="partner">
  <div class="partner-texture" role="img" aria-label="Dark close-up photo of illuminated keyboard and code"></div>
  <div class="partner-copy">
    <h2>Your Partner in Cyber Security</h2>
    <p>From first scoping call to final retest, we stay beside your team and turn findings into lasting security improvements.</p>
    <div class="actions"><span class="btn ghost">Our Story</span><span class="btn">Contact Us</span></div>
  </div>
</section>

<section class="consulting">
  <div class="wrap">
    <span class="tag">Why Us</span>
    <h2>Tailored Information Security Consulting</h2>
    <div class="pillars">
      <div class="pillar">
        <svg width="34" height="34" viewBox="0 0 34 34" fill="none" stroke="#f26b3a" stroke-width="2"><path d="M17 4l11 5v8c0 7-5 11-11 13C11 28 6 24 6 17V9z"/></svg>
        <div><h3>Identifying Regions</h3><p>We map where your data lives and which assets face the most risk.</p></div>
      </div>
      <div class="pillar">
        <svg width="34" height="34" viewBox="0 0 34 34" fill="none" stroke="#f26b3a" stroke-width="2"><circle cx="17" cy="12" r="6"/><path d="M6 30c1-7 6-10 11-10s10 3 11 10"/></svg>
        <div><h3>Expertise and Consultation</h3><p>Senior testers guide every project and advise on next steps.</p></div>
      </div>
      <div class="pillar">
        <svg width="34" height="34" viewBox="0 0 34 34" fill="none" stroke="#f26b3a" stroke-width="2"><path d="M8 18l6 6 12-14"/></svg>
        <div><h3>Customer Oriented</h3><p>Flexible scope, clear pricing and reports written for your team.</p></div>
      </div>
    </div>
    <p class="note">Every organisation is different, so every engagement is built around your goals, your systems and the threats you actually face.</p>
  </div>
</section>

<section class="contact">
  <div class="wrap">
    <div>
      <span class="tag">Contact</span>
      <h2>How Can We<br>Help You?</h2>
      <div class="contact-photo" role="img" aria-label="Photo of two colleagues reviewing a tablet"></div>
    </div>
    <div class="contact-form">
      <div class="field"><label>First Name</label><span></span></div>
      <div class="field"><label>Last Name</label><span></span></div>
      <div class="field"><label>Email Address</label><span></span></div>
      <div class="field"><label>Phone Number</label><span></span></div>
      <div class="field"><label>Company Name</label><span></span></div>
      <div class="field"><label>Subject</label><span></span></div>
      <div class="field full"><label>Message</label><span></span></div>
      <div><span class="btn">Send Enquiry</span></div>
    </div>
  </div>
</section>

<footer class="site-footer">
  <div class="wrap">
    <div>
      <div class="brand"><span class="brand-dot"></span>Emberstrata</div>
      <div class="socials"><i></i><i></i><i></i></div>
    </div>
    <div>
      <h4>Services</h4>
      <ul><li>Bug Bounty</li><li>Penetration Testing</li><li>Code Review</li></ul>
    </div>
    <div>
      <h4>Resources</h4>
      <ul><li>Blog</li><li>News</li><li>Case Studies</li></ul>
    </div>
    <div>
      <h4>Contact</h4>
      <ul><li>+61 2 5550 1482</li><li>hello@emberstrata.com.au</li></ul>
    </div>
  </div>
  <div class="footer-bar">
    <div class="wrap"><span>© Emberstrata. All rights reserved.</span><span>Privacy Policy · Terms of Use</span></div>
  </div>
</footer>

</body>
</html>
```